Opening new doors for every person - Solvane-Ridge

Please note that whoever will win this project , a 1on1 Powerpoint design project will separately be launched and will be offered to the winning designer.

---------
This letterhead is to provide proposals, as well as manuals for my clients.

I am looking for the letter, power point design and business card that inspires people when they see it, that they feel that design has been done with love and passion. Something that is professional, simple and yet creative, Business like, yet spiritual. That inspires growth!

This part of the branding for my company, therefore the business card as well as the power point design that will come after as 1on1 project should have the same team and feeling.

Solvane ridge, The company will be providing Coaching services (one-one or groups) to corporations, teams and individuals, partnering with them to achieve their goals/vision, by helping them to remove the self-imposed limiting beliefs, helping them to get them out of their own way, helping them to raise their level of consciousness and self-awareness.

The vision is: Bring conscious leadership to the workplace and to individuals for the wellbeing of humanity.

I know that somewhere out there will resonate with this, and will be inspired to provide the best design :) thank you very much!!!!!

MPORTANT:
- To use Free Fonts - let me know where I can download them
- Editable formats please for the double sized business card

LOGO is attached in pdf. If needed other file type please let me know

Thank you thank you in advance for your time and inspiration!! Sending good vibes for a great design out there

Must Have:
- Please keep on mind that the cards - power point will have the same feeling - Corporate branding
- that is not to heavy to look at it, that is simple and beautiful and inspiring
- Looking to have Calibri or Calibri light font

imple, yet inspirational - Professional, yet playful - business like, yet spiritual

I am looking for something different that the "standard" designs out there.

For example, the Logo of the company in the back side with a quote and the front side something simple, yet inspiring. that has the contact info as well as the social media details LinkedIn - Facebook - tweeter - website

Open for suggestions and inspiration :)

Thank you!

• - Please keep on mind that the cards - power point will have the same feeling
• - Corporate branding
• - that is not to heavy to look at it, that is simple and beautiful and inspiring
• - Looking to have Calibri or Calibri light font
• - Corporate colours as the logo

```html
<!DOCTYPE html>
<html lang="en">
<head>
<meta charset="utf-8">
<title>Solvane-Ridge Stationery</title>
<link href="https://fonts.googleapis.com/css2?family=Carlito:wght@400;700&family=Arimo:wght@400;700&family=Yellowtail&display=swap" rel="stylesheet">
<style>
  :root{
    --brand-blue:#17508c;
    --brand-yellow:#fbbf1a;
    --ink:#1f1f1f;
    --paper:#ffffff;
    --backdrop:#e9e9e9;
  }
  *{margin:0;padding:0;box-sizing:border-box}
  html,body{width:1189px;height:1200px;overflow:hidden}
  body{background:radial-gradient(circle at 50% 45%,#f6f6f6 0%,var(--backdrop) 70%);position:relative;font-family:"Arimo",sans-serif;color:var(--ink)}

  .brand-name{font-family:"Carlito",sans-serif;font-weight:400;color:var(--brand-blue);white-space:nowrap}

  /* Letterhead */
  .letterhead{position:absolute;left:273px;top:53px;width:647px;height:839px;background:var(--paper);box-shadow:0 2px 8px rgba(0,0,0,.06)}
  .letterhead .brand-name{position:absolute;left:54px;top:80px;font-size:26px}
  .contact-list{position:absolute;left:54px;top:183px;border-left:2px solid var(--brand-yellow);padding-left:9px;font-family:"Carlito",sans-serif;font-size:10.5px;line-height:12.5px;color:var(--brand-blue);list-style:none}
  .contact-list li{display:flex;align-items:center;gap:5px}
  .contact-list svg{width:9px;height:9px;flex:none}
  .recipient{position:absolute;left:54px;top:302px;font-size:11.5px;line-height:13.5px;font-style:normal}
  .recipient h2{font-size:13px;font-weight:700;margin-bottom:5px;letter-spacing:.2px}
  .letter-body{position:absolute;left:54px;top:394px;width:543px;font-size:11.8px;line-height:19.2px;letter-spacing:-.1px;text-align:justify}
  .letter-body p+p{margin-top:14px}
  .sign-off{position:absolute;left:54px;top:647px;font-size:12px}
  .signature{position:absolute;left:52px;top:672px;font-family:"Yellowtail",cursive;font-size:32px;line-height:40px;color:#222}
  .signer{position:absolute;left:54px;top:727px;font-size:12px;line-height:15px}
  .signer strong{font-size:13px}
  .letter-footer{position:absolute;left:0;bottom:8px;width:100%;height:24px;background:var(--brand-blue);color:#fff;font-family:"Carlito",sans-serif;font-size:10.5px;display:flex;align-items:center;justify-content:center;border-bottom:2px solid #fff}
  .letter-footer::after{content:"";position:absolute;left:0;right:0;top:24px;height:8px;background:var(--brand-yellow);transform:translateY(2px)}

  /* Business cards */
  .card{position:absolute;top:938px;width:319px;height:182px;border-radius:10px;overflow:hidden;box-shadow:0 2px 6px rgba(0,0,0,.06)}
  .card-front{left:273px;background:var(--brand-blue)}
  .card-back{left:603px;background:var(--paper)}
  .card .brand-name{position:absolute;left:0;width:100%;text-align:center;font-size:18px}
  .card-front .brand-name{top:78px;color:#fff}
  .card-back .brand-name{top:34px}
  .card-strip{position:absolute;left:0;bottom:0;width:100%;height:18px;background:var(--brand-yellow);color:var(--brand-blue);font-family:"Carlito",sans-serif;font-size:8.5px;display:flex;align-items:center;justify-content:center}
  .card-front .card-strip{letter-spacing:1px}
  .card-back-panel{position:absolute;left:0;top:97px;width:100%;height:67px;background:var(--brand-blue);color:#fff}
  .card-holder{position:absolute;right:174px;top:26px;text-align:right;font-family:"Carlito",sans-serif;line-height:9px}
  .card-holder strong{font-size:9px;letter-spacing:.3px}
  .card-holder span{display:block;font-size:8px;color:var(--brand-yellow)}
  .card-divider{position:absolute;left:154px;top:12px;width:1px;height:42px;background:var(--brand-yellow)}
  .card-back-panel .contact-list{left:162px;top:15px;border:0;padding:0;color:#fff;font-size:8.5px;line-height:10.5px}
  .card-back-panel .contact-list svg{width:8px;height:8px}
</style>
</head>
<body>

<section class="letterhead">
  <div class="brand-name">Solvane-Ridge</div>

  <ul class="contact-list">
    <li><svg viewBox="0 0 10 10"><circle cx="5" cy="5" r="5" fill="#fbbf1a"/><path d="M3 3h1.3l.5 1.4-.8.5a4 4 0 0 0 2 2l.5-.8 1.4.5V8A4.5 4.5 0 0 1 3 3z" fill="#fff"/></svg>+1.555.014.7720</li>
    <li><svg viewBox="0 0 10 10"><circle cx="5" cy="5" r="5" fill="#fbbf1a"/><rect x="2.6" y="3.3" width="4.8" height="3.4" fill="#fff"/><path d="M2.6 3.3 5 5.2 7.4 3.3" stroke="#fbbf1a" stroke-width=".6" fill="none"/></svg>hello@solvaneridge.net</li>
    <li><svg viewBox="0 0 10 10"><circle cx="5" cy="5" r="5" fill="#fbbf1a"/><circle cx="5" cy="5" r="2.6" stroke="#fff" stroke-width=".7" fill="none"/><path d="M2.4 5h5.2M5 2.4v5.2" stroke="#fff" stroke-width=".6"/></svg>www.solvaneridge.net</li>
  </ul>

  <address class="recipient">
    <h2>MARA ELLISON</h2>
    Street Name,City Name.<br>Zip Coad 0000
  </address>

  <div class="letter-body">
    <p>Lorem Ipsum is simply dummy text of the printing and typesetting industry. Lorem Ipsum has been the industry’s standard dummy text ever since the 1500s, when an unknown printer took a galley of type and scrambled it to make a type specimen book. It has survived not only five centuries,but also the leap into electronic typesetting, remaining essentially unchanged. It was popularised in the 1960s with the release of Letraset sheets containing Lorem Ipsum passages, and more recently with desktop publishing software like Aldus PageMaker including versions of Lorem Ipsum.</p>
    <p>It is a long established fact that a reader will be distracted by the readable content of a page when looking at its layout. The point of using Lorem Ipsum is that it has a more-or-less normal distribution of letters, as opposed to using ’Content here, content here’, making it look like readable English. Many desktop and web pages over the years, sometimes by accident, sometimes on purpose (injected humour and the like).</p>
  </div>

  <p class="sign-off">Regards,</p>
  <p class="signature">Theo Lindqvist</p>
  <p class="signer"><strong>Theo Lindqvist</strong><br>General Maneger</p>

  <footer class="letter-footer">Solvane-Ridge · Mindful Growth for Teams and People</footer>
</section>

<section class="card card-front">
  <div class="brand-name">Solvane-Ridge</div>
  <div class="card-strip">www.solvaneridge.net</div>
</section>

<section class="card card-back">
  <div class="brand-name">Solvane-Ridge</div>
  <div class="card-back-panel">
    <div class="card-holder"><strong>NADIA ORLOV</strong><span>Founder</span></div>
    <div class="card-divider"></div>
    <ul class="contact-list">
      <li><svg viewBox="0 0 10 10"><circle cx="5" cy="5" r="5" fill="#fbbf1a"/><path d="M3 3h1.3l.5 1.4-.8.5a4 4 0 0 0 2 2l.5-.8 1.4.5V8A4.5 4.5 0 0 1 3 3z" fill="#fff"/></svg>+1.555.014.7720</li>
      <li><svg viewBox="0 0 10 10"><circle cx="5" cy="5" r="5" fill="#fbbf1a"/><rect x="2.6" y="3.3" width="4.8" height="3.4" fill="#fff"/><path d="M2.6 3.3 5 5.2 7.4 3.3" stroke="#fbbf1a" stroke-width=".6" fill="none"/></svg>hello@solvaneridge.net</li>
      <li><svg viewBox="0 0 10 10"><circle cx="5" cy="5" r="5" fill="#fbbf1a"/><circle cx="5" cy="5" r="2.6" stroke="#fff" stroke-width=".7" fill="none"/><path d="M2.4 5h5.2M5 2.4v5.2" stroke="#fff" stroke-width=".6"/></svg>www.solvaneridge.net</li>
    </ul>
  </div>
  <div class="card-strip">Solvane-Ridge · Mindful Growth for Teams and People</div>
</section>

</body>
</html>
```